Business cards real estate company

We need a design for a business card. It is a company that specializes in real estate sales. There should be space for a photo of the respective employee as well as the website and telephone number on it. Design should be noble, innovative.

Contact Information for Business Card

Website, Name, Position, Telefonnummer

Requirements
Must have
• Photo, logo

```html
<!DOCTYPE html>
<html lang="en">
<head>
<meta charset="utf-8">
<title>Hearthvale – Business Card</title>
<link rel="stylesheet" href="https://fonts.googleapis.com/css2?family=Montserrat:wght@500;600&family=Arimo:wght@400&display=swap">
<style>
  :root {
    --stage: #2a2a2a;
    --card: #0b0b0b;
    --card-edge: #1c1c1c;
    --brand-green: #8cc63f;
    --name-green: #9ccb3b;
    --text-grey: #a7a7a7;
    --divider: #262626;
    --photo-bg: #ffffff;
    --photo-figure: #86888b;
    --back-logo: #d4d4d4;
  }
  * { box-sizing: border-box; margin: 0; padding: 0; }
  html, body {
    width: 1200px; height: 900px; overflow: hidden;
    background: var(--stage);
  }
  .stage {
    width: 1200px; height: 900px;
    display: flex; align-items: center; justify-content: center; gap: 40px;
  }
  .card {
    position: relative;
    width: 540px; height: 310px;
    background: var(--card);
    border: 1px solid var(--card-edge);
    border-radius: 22px;
    overflow: hidden;
  }
  .brand-name {
    font-family: "Montserrat", sans-serif;
    font-weight: 600;
    letter-spacing: 1px;
  }
  .card-front .brand-name {
    position: absolute; left: 40px; top: 30px;
    font-size: 60px; line-height: 1;
    color: var(--brand-green);
  }
  .portrait {
    position: absolute; left: 56px; top: 128px;
    width: 150px; height: 150px;
    background: linear-gradient(180deg, var(--photo-bg) 0%, var(--photo-bg) 35%, var(--photo-figure) 100%);
  }
  .divider {
    position: absolute; left: 228px; top: 128px;
    width: 1px; height: 150px;
    background: var(--divider);
  }
  .details {
    position: absolute; left: 250px; top: 132px;
    font-family: "Arimo", sans-serif;
  }
  .person-name {
    font-family: "Montserrat", sans-serif;
    font-weight: 500;
    font-size: 17px;
    letter-spacing: 0.3px;
    text-transform: uppercase;
    color: var(--name-green);
  }
  .person-role {
    margin-top: 2px;
    font-size: 14px;
    color: var(--text-grey);
  }
  .contact-list { list-style: none; margin-top: 38px; }
  .contact-item {
    display: flex; align-items: center; gap: 8px;
    font-size: 14px; line-height: 22px;
    color: var(--text-grey);
  }
  .contact-icon { width: 13px; height: 13px; flex: none; }
  .card-back { display: flex; align-items: center; justify-content: center; }
  .card-back .brand-name {
    font-size: 58px; line-height: 1;
    color: var(--back-logo);
  }
</style>
</head>
<body>
<main class="stage">
  <section class="card card-front" aria-label="Business card front">
    <div class="brand-name">Hearthvale</div>
    <div class="portrait" role="img" aria-label="Portrait photo of the employee"></div>
    <div class="divider"></div>
    <div class="details">
      <p class="person-name">Daniel Hartmann</p>
      <p class="person-role">Managing Director</p>
      <ul class="contact-list">
        <li class="contact-item">
          <svg class="contact-icon" viewBox="0 0 24 24" aria-hidden="true">
            <path fill="var(--brand-green)" d="M6.6 10.8a15.1 15.1 0 0 0 6.6 6.6l2.2-2.2a1 1 0 0 1 1-.25 11.4 11.4 0 0 0 3.6.57 1 1 0 0 1 1 1V20a1 1 0 0 1-1 1A17 17 0 0 1 3 4a1 1 0 0 1 1-1h3.5a1 1 0 0 1 1 1c0 1.25.2 2.45.57 3.57a1 1 0 0 1-.25 1z"/>
          </svg>
          044-555 010 020
        </li>
        <li class="contact-item">
          <svg class="contact-icon" viewBox="0 0 24 24" aria-hidden="true">
            <g fill="none" stroke="var(--brand-green)" stroke-width="2">
              <circle cx="12" cy="12" r="10"/>
              <ellipse cx="12" cy="12" rx="4.5" ry="10"/>
              <path d="M2 12h20M4 7h16M4 17h16"/>
            </g>
          </svg>
          www.hearthvale.com
        </li>
      </ul>
    </div>
  </section>

  <section class="card card-back" aria-label="Business card back">
    <div class="brand-name">Hearthvale</div>
  </section>
</main>
</body>
</html>
```